Redesign website for Breeze Haven

Breeze Haven Algarve (www.breezehavenalgarve.com) is a vacation rental company based in Algarve, Portugal.
We want to redesign our website for a more modern and responsive version.

We do like something like this: https://www.marblenook.com, https://www.tallpinelodge.com, http://www.kestrelhomesqz.com, and https://www.trevalmo.com

We would prefer the use of a Wordpress theme specific for vacation rentals, that already has the tools that we need: reservations, availability sync via Ical, and payments.

Target Market(s)

The website must be appealing to guests who book directly, and to property owners, who deliver their villas to our portfolio.

Industry/Entity Type

Accommodation

Coding

Coded - Design and coding required

Font styles to use
Sans Serif

Colors
33a6d7
85cae6
cee9f5
cfeae6
86cfc6

Requirements
Must have
• A summery and holiday look

```html
<!DOCTYPE html>
<html lang="en">
<head>
<meta charset="utf-8">
<title>Breeze Haven – The Algarve Holiday Collection</title>
<link href="https://fonts.googleapis.com/css2?family=Roboto:ital,wght@0,300;0,400;0,500;0,700;1,400&display=swap" rel="stylesheet">
<style>
:root{
  --blue:#33a6d7;
  --blue-soft:#85cae6;
  --blue-pale:#cee9f5;
  --mint-pale:#cfeae6;
  --teal:#86cfc6;
  --ink:#2b2b2b;
  --text:#555;
  --muted:#888;
  --line:#e4e4e4;
  --footer:#1f2022;
  --navy:rgba(12,22,36,.88);
  --star:#f2c230;
}
*{box-sizing:border-box;margin:0;padding:0}
html,body{width:1200px;height:3991px;overflow:hidden}
body{font-family:"Roboto",Arial,sans-serif;color:var(--text);background:#fff;position:relative}
.abs{position:absolute}
a{color:inherit;text-decoration:none}

/* header */
.site-header{position:absolute;top:0;left:0;width:1200px;height:96px;background:#fff}
.brand{position:absolute;left:40px;top:26px;font-weight:300;font-size:31px;letter-spacing:2px;color:var(--blue);text-transform:uppercase}
.main-nav{position:absolute;right:30px;top:38px;display:flex;gap:28px;font-size:14px;font-weight:500;color:var(--ink);text-transform:uppercase}
.main-nav .phone{color:var(--blue);font-weight:700;font-size:16px;display:flex;align-items:center;gap:6px;margin-top:-2px}

/* hero */
.hero{position:absolute;top:96px;left:0;width:1200px;height:591px;
  background:linear-gradient(180deg,#6d88a3 0%,#8d7e6e 30%,#4c6d82 55%,#1f5f93 75%,#0f3552 100%)}
.hero-kicker{position:absolute;top:142px;width:100%;text-align:center;color:#fff;font-weight:300;font-size:42px;letter-spacing:3px}
.hero-title{position:absolute;top:194px;width:100%;text-align:center;color:#fff;font-weight:700;font-size:48px;line-height:54px;text-transform:uppercase}
.btn{display:inline-block;background:var(--teal);color:#fff;font-weight:500;text-transform:uppercase;text-align:center}
.hero .btn{position:absolute;left:543px;top:318px;width:114px;height:34px;line-height:34px;font-size:13px}
.hero-arrow{position:absolute;top:270px}
.booking{position:absolute;left:98px;top:457px;width:1004px;height:134px;background:var(--navy);border-top:5px solid var(--teal)}
.field{position:absolute;top:22px}
.field label{display:block;color:#fff;font-weight:700;font-size:14px;text-transform:uppercase;margin-bottom:14px}
.field .input{width:200px;height:38px;background:#fff;border:1px solid #ccc;font-size:12px;color:#999;line-height:36px;padding-left:10px;position:relative}
.field .input svg{position:absolute;right:9px;top:12px}
.booking .btn{position:absolute;left:878px;top:58px;width:108px;height:38px;line-height:38px;font-size:13px}

/* rentals */
.section-title{position:absolute;width:100%;text-align:center;font-size:32px;font-weight:500;color:var(--ink);text-transform:uppercase}
.card{position:absolute;width:314px;height:359px;background:#fff;box-shadow:0 2px 8px rgba(0,0,0,.14)}
.card .photo{height:181px}
.card h3{margin-top:22px;text-align:center;font-size:15px;font-weight:400;color:#444}
.card p{margin:12px 30px 0;text-align:center;font-size:11.5px;line-height:17px;color:#666}
.card .foot{position:absolute;left:0;right:0;bottom:0;height:58px;border-top:1px solid var(--line);padding:12px 14px}
.card .from{font-size:10px;color:#555;text-transform:uppercase}
.card .price{font-size:16px;color:var(--blue)}
.card .btn-sm{position:absolute;right:14px;top:18px;background:var(--blue);color:#fff;font-size:10px;font-weight:700;padding:5px 9px;text-transform:uppercase;border-radius:2px}

/* amenities band */
.amenities{position:absolute;top:1636px;left:0;width:1200px;height:485px;background:linear-gradient(100deg,#2f9fd3 0%,var(--blue) 50%,#5ab6dd 100%)}
.amenities h2{position:absolute;top:80px;width:100%;text-align:center;color:#fff;font-size:30px;font-weight:500;text-transform:uppercase}
.amenities p{position:absolute;top:132px;left:200px;width:800px;text-align:center;color:#fff;font-size:13.5px;line-height:22px}
.amenity{position:absolute;top:261px;width:160px;text-align:center;color:#fff}
.amenity .ring{width:100px;height:100px;margin:0 auto;border:2px solid #fff;border-radius:50%;display:flex;align-items:center;justify-content:center}
.amenity span{display:block;margin-top:26px;font-size:15px;font-weight:700;text-transform:uppercase}

/* why book */
.why-frame{position:absolute;left:108px;top:2192px;width:390px;height:290px;background:var(--teal)}
.why-photo{position:absolute;left:98px;top:2205px;width:390px;height:283px;background:linear-gradient(180deg,#7f8fa5 0%,#c4a27a 45%,#5b5956 70%,#2c2c2e 100%)}
.why h2{position:absolute;left:538px;top:2208px;font-size:33px;font-weight:500;color:var(--ink);text-transform:uppercase}
.why p{position:absolute;left:538px;top:2268px;width:560px;font-size:13px;line-height:21px;color:#666}
.why ul{position:absolute;left:538px;top:2380px;list-style:none;font-size:13px;color:#555}
.why li{display:flex;align-items:center;gap:12px;height:26px}

/* reviews */
.reviews{position:absolute;top:2594px;left:0;width:1200px;height:466px;background:linear-gradient(180deg,var(--mint-pale),#d9efec)}
.reviews h2{position:absolute;top:68px;width:100%;text-align:center;font-size:32px;font-weight:500;color:var(--ink);text-transform:uppercase}
.review{position:absolute;top:143px;width:320px;height:152px;background:#fff;padding:22px 22px 0}
.review q{display:block;font-style:italic;font-size:11px;line-height:17px;color:#999;quotes:"\201C" "\201D"}
.review .who{margin-top:10px;font-style:italic;font-size:13px;color:var(--blue)}
.review .stars{position:absolute;left:22px;top:172px;display:flex;gap:4px}
.review .avatar{position:absolute;right:16px;top:112px;width:82px;height:82px;border-radius:50%;border:4px solid #fff;box-shadow:0 1px 4px rgba(0,0,0,.2)}
.dots{position:absolute;top:400px;left:566px;display:flex;gap:5px}
.dots i{width:12px;height:12px;border:2px solid #333;border-radius:50%}

/* events */
.events h2{position:absolute;left:98px;top:3128px;font-size:32px;font-weight:500;color:var(--ink);text-transform:uppercase}
.ev-nav{position:absolute;left:1078px;top:3139px;display:flex;gap:6px}
.event .pic{position:absolute;width:176px;height:176px;border-radius:50%;border:5px solid #fff;box-shadow:0 0 0 1px #ddd}
.event h3{position:absolute;font-size:17px;font-weight:400;color:#333}
.event .date{position:absolute;background:var(--blue);color:#fff;font-size:11px;font-weight:700;padding:5px 10px}
.event p{position:absolute;width:250px;font-size:12.5px;line-height:20px;color:#555}
.event .more{position:absolute;font-size:13px;color:#555}

/* footer */
.site-footer{position:absolute;top:3473px;left:0;width:1200px;height:518px;background:var(--footer)}
.site-footer h4{position:absolute;top:70px;color:#fff;font-size:19px;font-weight:500;text-transform:uppercase}
.quick{position:absolute;left:98px;top:126px;list-style:none;color:#fff;font-size:12.5px}
.quick li{height:24px}
.foot-brand{position:absolute;left:98px;top:270px;color:#fff;font-weight:300;font-size:27px;letter-spacing:2px;text-transform:uppercase}
.form-field{position:absolute;left:399px;width:384px;height:34px;background:#fff;font-size:11px;color:#666;padding:9px 10px}
.submit{position:absolute;left:399px;top:356px;width:227px;height:40px;line-height:40px;font-size:14px}
.contact-row{position:absolute;left:849px;display:flex;gap:16px;color:#fff;font-size:12px;line-height:18px}
.socials{position:absolute;left:849px;top:292px;display:flex;gap:6px}
.socials i{width:18px;height:18px;border:1px solid #bbb;border-radius:50%}
.copyright{position:absolute;top:3944px;width:100%;text-align:center;color:#ddd;font-size:11px}
</style>
</head>
<body>

<header class="site-header">
  <div class="brand">Breeze Haven</div>
  <nav class="main-nav">
    <a>Home</a><a>Holiday Rentals</a><a>What to do</a><a>Guest Services</a><a>Reviews</a>
    <a class="phone"><svg width="15" height="15" viewBox="0 0 24 24"><path fill="#33a6d7" d="M6.6 10.8a15.1 15.1 0 0 0 6.6 6.6l2.2-2.2c.3-.3.7-.4 1-.2 1.1.4 2.3.6 3.6.6.6 0 1 .4 1 1V20c0 .6-.4 1-1 1A17 17 0 0 1 3 4c0-.6.4-1 1-1h3.5c.6 0 1 .4 1 1 0 1.3.2 2.5.6 3.6.1.3 0 .7-.2 1z"/></svg>555-214-7730</a>
  </nav>
</header>

<section class="hero" role="img" aria-label="Photo of a villa complex with a curved swimming pool at dusk">
  <svg class="hero-arrow" style="left:40px" width="16" height="22" viewBox="0 0 16 22"><path d="M12 3 4 11l8 8" stroke="#fff" stroke-width="3" fill="none"/></svg>
  <svg class="hero-arrow" style="right:40px" width="16" height="22" viewBox="0 0 16 22"><path d="m4 3 8 8-8 8" stroke="#fff" stroke-width="3" fill="none"/></svg>
  <div class="hero-kicker">BREEZE HAVEN</div>
  <h1 class="hero-title">The Algarve Holiday<br>Collection</h1>
  <a class="btn">Read more</a>
  <form class="booking">
    <div class="field" style="left:26px"><label>Check-in</label><div class="input">Check-in Date<svg width="12" height="12" viewBox="0 0 12 12"><rect x="1" y="2" width="10" height="9" fill="none" stroke="#666"/><path d="M1 5h10" stroke="#666"/></svg></div></div>
    <div class="field" style="left:236px"><label>Check-out</label><div class="input">Check-in Date<svg width="12" height="12" viewBox="0 0 12 12"><rect x="1" y="2" width="10" height="9" fill="none" stroke="#666"/><path d="M1 5h10" stroke="#666"/></svg></div></div>
    <div class="field" style="left:446px"><label>Adults</label><div class="input">2<svg width="10" height="10" viewBox="0 0 10 10"><path d="M1 3h8L5 8z" fill="#666"/></svg></div></div>
    <div class="field" style="left:656px"><label>Children</label><div class="input">0<svg width="10" height="10" viewBox="0 0 10 10"><path d="M1 3h8L5 8z" fill="#666"/></svg></div></div>
    <a class="btn">Book now</a>
  </form>
</section>

<h2 class="section-title" style="top:728px">Vacation Rental</h2>

<article class="card" style="left:98px;top:812px"><div class="photo" role="img" aria-label="Bright twin bedroom" style="background:linear-gradient(135deg,#f1ede4,#d9cbb0)"></div><h3>Nemo enim ipsam voluptatem</h3><p>Sed ut perspiciatis unde omnis iste natus error sit voluptatem accusantium doloremque</p><div class="foot"><div class="from">Starts from</div><div class="price">$ 2644</div><span class="btn-sm">Read more</span></div></article>
<article class="card" style="left:442px;top:812px"><div class="photo" role="img" aria-label="Pool terrace under palm trees" style="background:linear-gradient(135deg,#5f8a4a,#a9b888 60%,#c8c2a8)"></div><h3>Nemo enim ipsam voluptatem</h3><p>Sed ut perspiciatis unde omnis iste natus error sit voluptatem accusantium doloremque</p><div class="foot"><div class="from">Starts from</div><div class="price">$ 2644</div><span class="btn-sm">Read more</span></div></article>
<article class="card" style="left:785px;top:812px"><div class="photo" role="img" aria-label="White villa with garden steps" style="background:linear-gradient(180deg,#a8c6de,#e8dfcf 50%,#5d8a4c)"></div><h3>Nemo enim ipsam voluptatem</h3><p>Sed ut perspiciatis unde omnis iste natus error sit voluptatem accusantium doloremque</p><div class="foot"><div class="from">Starts from</div><div class="price">$ 2644</div><span class="btn-sm">Read more</span></div></article>
<article class="card" style="left:98px;top:1197px"><div class="photo" role="img" aria-label="Modern hallway with staircase and plants" style="background:linear-gradient(135deg,#e9ece8,#a9b59a 60%,#6f7d5d)"></div><h3>Nemo enim ipsam voluptatem</h3><p>Sed ut perspiciatis unde omnis iste natus error sit voluptatem accusantium doloremque</p><div class="foot"><div class="from">Starts from</div><div class="price">$ 2644</div><span class="btn-sm">Read more</span></div></article>
<article class="card" style="left:442px;top:1197px"><div class="photo" role="img" aria-label="Lit pool at night" style="background:linear-gradient(180deg,#2b2f3a,#6b5a48 45%,#2f7fb8)"></div><h3>Nemo enim ipsam voluptatem</h3><p>Sed ut perspiciatis unde omnis iste natus error sit voluptatem accusantium doloremque</p><div class="foot"><div class="from">Starts from</div><div class="price">$ 2644</div><span class="btn-sm">Read more</span></div></article>
<article class="card" style="left:785px;top:1197px"><div class="photo" role="img" aria-label="Villa facade with pool at dusk" style="background:linear-gradient(180deg,#3f5f8e,#8c7b86 50%,#3d9ac4)"></div><h3>Nemo enim ipsam voluptatem</h3><p>Sed ut perspiciatis unde omnis iste natus error sit voluptatem accusantium doloremque</p><div class="foot"><div class="from">Starts from</div><div class="price">$ 2644</div><span class="btn-sm">Read more</span></div></article>

<section class="amenities">
  <h2>Breeze Haven – The Algarve Holiday Collection</h2>
  <p>We think style may be also accessible, so we choose really cool houses in our naturally beautiful Algarve just for you. With us you can experience not only stylish villas, but also family retreats at their very best. In the Algarve the beach is stunning, the entertainment and restaurants incredible, the golf courses amazing. All that plus the option to enjoy our cool services &amp; activities!</p>
  <div class="amenity" style="left:109px"><div class="ring"><svg width="48" height="40" viewBox="0 0 48 40" fill="none" stroke="#fff" stroke-width="3" stroke-linecap="round"><path d="M4 14a28 28 0 0 1 40 0"/><path d="M11 21a18 18 0 0 1 26 0"/><path d="M18 28a8 8 0 0 1 12 0"/><circle cx="24" cy="35" r="2" fill="#fff"/></svg></div><span>Wifi</span></div>
  <div class="amenity" style="left:279px"><div class="ring"><svg width="40" height="48" viewBox="0 0 40 48" fill="none" stroke="#fff" stroke-width="3"><path d="M10 4h20l6 18H4z"/><path d="M20 22v16M10 42h20"/></svg></div><span>Fully Furnished</span></div>
  <div class="amenity" style="left:449px"><div class="ring"><svg width="52" height="44" viewBox="0 0 52 44" fill="none" stroke="#fff" stroke-width="3"><rect x="32" y="2" width="16" height="16"/><path d="M37 14V6h4a3 3 0 0 1 0 6h-4"/><path d="M6 30l4-10h22l4 10v8H6z"/><circle cx="12" cy="33" r="2" fill="#fff"/><circle cx="30" cy="33" r="2" fill="#fff"/></svg></div><span>Free Parking</span></div>
  <div class="amenity" style="left:619px"><div class="ring"><svg width="46" height="46" viewBox="0 0 24 24"><path fill="#fff" d="M21 16v-2l-8-5V3.5a1.5 1.5 0 0 0-3 0V9l-8 5v2l8-2.5V19l-2 1.5V22l3.5-1 3.5 1v-1.5L13 19v-5.5z"/></svg></div><span>Airport Transfers</span></div>
  <div class="amenity" style="left:789px"><div class="ring"><svg width="46" height="46" viewBox="0 0 46 46" fill="none" stroke="#fff" stroke-width="3" stroke-linecap="round"><path d="M40 6 22 24"/><path d="M22 24c-6-2-12 2-14 8l-2 8c8 0 14-2 18-8 2-3 0-6-2-8z"/><path d="M11 38l5-7M16 39l4-6"/></svg></div><span>Cleaning Services</span></div>
</section>

<section class="why">
  <div class="why-frame"></div>
  <div class="why-photo" role="img" aria-label="Rooftop terrace lounge with sea view at sunset"></div>
  <h2>Why book with us</h2>
  <p>Nemo enim ipsam voluptatem quia voluptas sit aspernatur aut odit aut fugit, sed quia consequuntur magni dolores eos qui ratione voluptatem sequi nesciunt. Neque porro quisquam est, qui dolorem ipsum quia dolor sit amet, consectetur, adipisci velit, sed quia non numquam eius modi tempora incidunt ut labore et dolore magnam aliquam quaerat voluptatem.</p>
  <ul>
    <li><svg width="12" height="12" viewBox="0 0 12 12"><circle cx="6" cy="6" r="6" fill="#86cfc6"/><path d="m3 6 2 2 4-4" stroke="#fff" stroke-width="1.5" fill="none"/></svg>Light and under stated luxury</li>
    <li><svg width="12" height="12" viewBox="0 0 12 12"><circle cx="6" cy="6" r="6" fill="#86cfc6"/><path d="m3 6 2 2 4-4" stroke="#fff" stroke-width="1.5" fill="none"/></svg>Stylishly contemporary villas</li>
    <li><svg width="12" height="12" viewBox="0 0 12 12"><circle cx="6" cy="6" r="6" fill="#86cfc6"/><path d="m3 6 2 2 4-4" stroke="#fff" stroke-width="1.5" fill="none"/></svg>Exceptional service with Portuguese simpathy</li>
    <li><svg width="12" height="12" viewBox="0 0 12 12"><circle cx="6" cy="6" r="6" fill="#86cfc6"/><path d="m3 6 2 2 4-4" stroke="#fff" stroke-width="1.5" fill="none"/></svg>Guests that return and recommend</li>
  </ul>
</section>

<section class="reviews">
  <h2>Breeze Haven Reviews</h2>
  <div class="review" style="left:98px"><q>Nemo enim ipsam voluptatem quia voluptas sit aspernatur aut odit aut fugit, sed quia consequuntur magni dolores eos qui ratione voluptatem sequi nesciunt. Neque porro quisquam est.</q><div class="who">- Sam Rivers</div><div class="stars"><svg width="70" height="12" viewBox="0 0 70 12"><g fill="#f2c230"><circle cx="6" cy="6" r="5"/><circle cx="20" cy="6" r="5"/><circle cx="34" cy="6" r="5"/></g><g fill="#555"><circle cx="48" cy="6" r="5"/><circle cx="62" cy="6" r="5"/></g></svg></div><div class="avatar" role="img" aria-label="Guest portrait" style="background:linear-gradient(180deg,#c9b7a3,#6d6259)"></div></div>
  <div class="review" style="left:442px"><q>Nemo enim ipsam voluptatem quia voluptas sit aspernatur aut odit aut fugit, sed quia consequuntur magni dolores eos qui ratione voluptatem sequi nesciunt. Neque porro quisquam est.</q><div class="who">- Sam Rivers</div><div class="stars"><svg width="70" height="12" viewBox="0 0 70 12"><g fill="#f2c230"><circle cx="6" cy="6" r="5"/><circle cx="20" cy="6" r="5"/><circle cx="34" cy="6" r="5"/></g><g fill="#555"><circle cx="48" cy="6" r="5"/><circle cx="62" cy="6" r="5"/></g></svg></div><div class="avatar" role="img" aria-label="Guest portrait" style="background:linear-gradient(180deg,#d98a4e,#f0d9c4)"></div></div>
  <div class="review" style="left:785px"><q>Nemo enim ipsam voluptatem quia voluptas sit aspernatur aut odit aut fugit, sed quia consequuntur magni dolores eos qui ratione voluptatem sequi nesciunt. Neque porro quisquam est.</q><div class="who">- Sam Rivers</div><div class="stars"><svg width="70" height="12" viewBox="0 0 70 12"><g fill="#f2c230"><circle cx="6" cy="6" r="5"/><circle cx="20" cy="6" r="5"/><circle cx="34" cy="6" r="5"/></g><g fill="#555"><circle cx="48" cy="6" r="5"/><circle cx="62" cy="6" r="5"/></g></svg></div><div class="avatar" role="img" aria-label="Guest portrait" style="background:linear-gradient(180deg,#5a4636,#d8c2ab)"></div></div>
  <div class="dots"><i></i><i></i><i></i><i></i></div>
</section>

<section class="events">
  <h2>Latest Events</h2>
  <div class="ev-nav"><svg width="10" height="14" viewBox="0 0 10 14"><path d="M7 2 2 7l5 5" stroke="#333" stroke-width="2" fill="none"/></svg><svg width="10" height="14" viewBox="0 0 10 14"><path d="m3 2 5 5-5 5" stroke="#333" stroke-width="2" fill="none"/></svg></div>
  <div class="event">
    <div class="pic" role="img" aria-label="Evening dinner party event" style="left:98px;top:3214px;background:radial-gradient(circle at 40% 40%,#f3d9d0,#b7704f 70%,#6a3b2c)"></div>
    <h3 style="left:303px;top:3210px">Nulla at diam ornare, aliquam</h3>
    <span class="date" style="left:303px;top:3243px">Feb 25, 2018</span>
    <p style="left:303px;top:3280px">Nulla at diam ornare, aliquam urna vel, modo urna. Nam id risus a est luctus consectetur quis eget libero. Suspendisse potenti. Pellentesque habitant</p>
    <span class="more" style="left:303px;top:3383px">Read More +</span>
  </div>
  <div class="event">
    <div class="pic" role="img" aria-label="Lantern-lit garden at night" style="left:642px;top:3214px;background:radial-gradient(circle at 50% 55%,#f1c76a,#7b5a2c 55%,#1d1a17)"></div>
    <h3 style="left:845px;top:3210px">Nulla at diam ornare, aliquam</h3>
    <span class="date" style="left:845px;top:3243px">Feb 25, 2018</span>
    <p style="left:845px;top:3280px">Nulla at diam ornare, aliquam urna vel, modo urna. Nam id risus a est luctus consectetur quis eget libero. Suspendisse potenti. Pellentesque habitant</p>
    <span class="more" style="left:845px;top:3383px">Read More +</span>
  </div>
</section>

<footer class="site-footer">
  <svg class="abs" style="left:0;top:-30px" width="1200" height="60" viewBox="0 0 1200 60" preserveAspectRatio="none">
    <path d="M0 32C300 8 700 8 1200 28V60H0z" fill="#1f2022"/>
    <path d="M0 32C300 8 700 8 1200 28" stroke="#33a6d7" stroke-width="5" fill="none"/>
    <path d="M0 24C350 4 800 2 1200 20" stroke="#85cae6" stroke-width="2" fill="none"/>
  </svg>
  <h4 style="left:98px">Quick Links</h4>
  <ul class="quick"><li>About Us</li><li>Terms &amp; Conditions</li><li>List your Property</li><li>Rent a Car</li><li>Contact Us</li></ul>
  <div class="foot-brand">Breeze Haven</div>

  <h4 style="left:399px">Book Appointment</h4>
  <div class="form-field" style="top:128px">Name</div>
  <div class="form-field" style="top:170px">Phone number</div>
  <div class="form-field" style="top:212px">Email address</div>
  <div class="form-field" style="top:254px;height:80px">Enquiry</div>
  <a class="btn submit">Submit</a>

  <h4 style="left:849px">Contact Us</h4>
  <div class="contact-row" style="top:126px"><svg width="16" height="20" viewBox="0 0 16 20"><path d="M8 1a6 6 0 0 0-6 6c0 5 6 12 6 12s6-7 6-12a6 6 0 0 0-6-6z" fill="none" stroke="#fff" stroke-width="1.5"/><circle cx="8" cy="7" r="2" fill="#fff"/></svg><div>BREEZE HAVEN<br>Rua das Gaivotas, Lote 12<br>Albufeira - Portugal</div></div>
  <div class="contact-row" style="top:200px"><svg width="16" height="16" viewBox="0 0 24 24"><path fill="#fff" d="M6.6 10.8a15.1 15.1 0 0 0 6.6 6.6l2.2-2.2c.3-.3.7-.4 1-.2 1.1.4 2.3.6 3.6.6.6 0 1 .4 1 1V20c0 .6-.4 1-1 1A17 17 0 0 1 3 4c0-.6.4-1 1-1h3.5c.6 0 1 .4 1 1 0 1.3.2 2.5.6 3.6.1.3 0 .7-.2 1z"/></svg><div>Phone: +(351) 900 555 018</div></div>
  <div class="contact-row" style="top:240px"><svg width="16" height="14" viewBox="0 0 16 14"><rect x="1" y="1" width="14" height="12" fill="none" stroke="#fff" stroke-width="1.5"/><path d="m1 2 7 6 7-6" fill="none" stroke="#fff" stroke-width="1.5"/></svg><div>info@breezehavenalgarve.com</div></div>
  <div class="socials"><i></i><i></i><i></i><i></i></div>
</footer>
<div class="copyright">2018 © Copyrights BREEZE HAVEN.All Rights Reserved</div>

</body>
</html>
```